Willow Glow & Laser - Business Banner with Brand Elements

Design:
• We would like to get a creative design for a wide banner that will go outside our medical spa clinic location. We need a designer to make a simple yet colorful and high-quality design layout. We want this banner to be eye-catching and to communicate the services we offer at our business: Laser Hair Removal | Velonix | Lip Filler.

Requirements:
• We would like the banner to include our companies information which is the following:

Logo
“Refresh Your Skin”
Laser Hair Removal | Velonix | Lip Filler
(555) 287-1936
www.WillowGlowLaser.com

Colors:
• Our business colors are orange, a hint of black and white, but mostly peach/orange tones. (Orange: #f78f20 , White: #ffffff)

Fonts:
• Josefins Sans Bold & Lato

Content and images can be located here:
https://files.cloudvaultshare.com/folders/7tQmZ2xVbR9kLpN4sW8yH3cD6fJ1gA0eU?usp=sharing

The following will give you an idea of our brand presentation:
• Our website is: www.WillowGlowLaser.com
• Our Instagram; @willowglowlaser
• Our Facebook: www.socialpagehub.com/willowglowlaser

Target Market(s)
• Women 25 - 45

Industry/Entity Type
• Beauty

```html
<!DOCTYPE html>
<html lang="en">
<head>
<meta charset="utf-8">
<title>Willow Glow &amp; Laser – Outdoor Banner</title>
<link rel="stylesheet" href="https://fonts.googleapis.com/css2?family=Josefin+Sans:wght@700&family=Lato:wght@300;400;700&display=swap">
<style>
  :root {
    --orange: #f78f20;
    --orange-deep: #cf7418;
    --black: #111111;
    --white: #ffffff;
    --grey: #4a4a4a;
    --photo-cool: #7fcad8;
    --photo-warm: #d8b48c;
  }
  html, body {
    margin: 0;
    padding: 0;
    width: 1200px;
    height: 480px;
    overflow: hidden;
    background: var(--white);
  }
  .banner {
    position: relative;
    width: 1200px;
    height: 480px;
    overflow: hidden;
    background: var(--white);
  }
  .banner__art {
    position: absolute;
    inset: 0;
  }
  .brand {
    position: absolute;
    top: 42px;
    left: 872px;
    display: flex;
    align-items: center;
    gap: 12px;
  }
  .brand__dot {
    width: 40px;
    height: 40px;
    border-radius: 50%;
    background: var(--orange);
  }
  .brand__name {
    font-family: "Josefin Sans", sans-serif;
    font-weight: 700;
    font-size: 24px;
    color: var(--black);
    padding-top: 4px;
  }
  .headline {
    position: absolute;
    left: 800px;
    top: 166px;
    width: 358px;
    margin: 0;
    font-family: "Josefin Sans", sans-serif;
    font-weight: 700;
    font-size: 66px;
    line-height: 60px;
    letter-spacing: -0.5px;
    color: var(--orange);
  }
  .headline__line { display: block; }
  .headline__line--second { text-align: right; }
  .headline__accent { color: var(--black); }
  .services {
    position: absolute;
    left: 801px;
    top: 313px;
    width: 357px;
    margin: 0;
    font-family: "Lato", sans-serif;
    font-weight: 700;
    font-size: 19px;
    color: var(--grey);
    white-space: nowrap;
    display: flex;
    justify-content: space-between;
  }
  .services__sep { font-weight: 400; }
  .divider {
    position: absolute;
    left: 801px;
    top: 356px;
    width: 357px;
    height: 12px;
  }
  .contact {
    position: absolute;
    left: 800px;
    top: 386px;
    width: 360px;
    text-align: center;
    font-family: "Lato", sans-serif;
    color: var(--black);
  }
  .contact__phone {
    display: block;
    font-weight: 300;
    font-size: 35px;
    line-height: 42px;
  }
  .contact__web {
    display: block;
    font-weight: 400;
    font-size: 18px;
    line-height: 24px;
  }
  .contact__web strong { font-weight: 700; }
</style>
</head>
<body>
<main class="banner">
  <svg class="banner__art" width="1200" height="480" viewBox="0 0 1200 480" xmlns="http://www.w3.org/2000/svg">
    <defs>
      <linearGradient id="photo-tones" x1="0" y1="0" x2="1" y2="1">
        <stop offset="0" stop-color="var(--photo-cool)"/>
        <stop offset="1" stop-color="var(--photo-warm)"/>
      </linearGradient>
    </defs>
    <rect class="band-orange" x="0" y="0" width="320" height="480" fill="var(--orange)"/>
    <circle class="band-shadow" cx="412" cy="262" r="344" fill="var(--orange-deep)"/>
    <circle class="photo-ring" cx="430" cy="240" r="344" fill="var(--white)"/>
    <circle class="photo" cx="430" cy="240" r="334" fill="url(#photo-tones)"
            role="img" aria-label="Photo of a smiling woman in a straw sun hat on a sunny beach"/>
    <path class="photo-cutout" fill="var(--white)"
          d="M378 400 C 318 340, 272 250, 278 170 C 284 80, 340 10, 420 -20 L 520 -20 C 500 40, 470 110, 448 180 C 424 260, 398 330, 378 400 Z"/>
  </svg>

  <div class="brand">
    <span class="brand__dot"></span>
    <span class="brand__name">Willow Glow &amp; Laser</span>
  </div>

  <h1 class="headline">
    <span class="headline__line"><span class="headline__accent">Re</span>fresh</span>
    <span class="headline__line headline__line--second">Your Skin</span>
  </h1>

  <p class="services">
    <span>Laser Hair Removal</span>
    <span class="services__sep">|</span>
    <span>Velonix</span>
    <span class="services__sep">|</span>
    <span>Lip Filler</span>
  </p>

  <svg class="divider" viewBox="0 0 360 12" preserveAspectRatio="none" xmlns="http://www.w3.org/2000/svg" aria-hidden="true">
    <path d="M0 6 q6 -5 12 0 t12 0 t12 0 t12 0 t12 0 t12 0 t12 0 t12 0 t12 0 t12 0 t12 0 t12 0 t12 0 t12 0 t12 0 t12 0 t12 0 t12 0 t12 0 t12 0 t12 0 t12 0 t12 0 t12 0 t12 0 t12 0 t12 0 t12 0 t12 0 t12 0"
          fill="none" stroke="var(--orange)" stroke-width="1.6"/>
  </svg>

  <div class="contact">
    <span class="contact__phone">(555) 287-1936</span>
    <span class="contact__web">www.<strong>WillowGlowLaser</strong>.com</span>
  </div>
</main>
</body>
</html>
```